11 x 11 Flyer Design for Social Media - Reverse Mortgages

62 or older?

A Reverse Mortgage
could be
Your Road to Financial Freedom

* No Monthly Payments
* No Income Requirements
* No Credit Score Requirements
* No Loss of Ownership

Receive cash by lump sum, monthly installments or a line of credit!!

Call us today for a Free Consultation!!
(800) 647-2915

Harborline Financial Services, Inc.
NMLS #517830
www.harborlinefunds.example

```html
<!DOCTYPE html>
<html lang="en">
<head>
<meta charset="utf-8">
<title>Reverse Mortgage Flyer – Harborline Financial Services</title>
<link rel="stylesheet" href="https://fonts.googleapis.com/css2?family=Rubik:wght@500;600;700&family=Roboto+Condensed:wght@600;700&display=swap">
<style>
  :root {
    --blue: #1b6aa8;
    --blue-deep: #13598f;
    --green: #97e52a;
    --lime: #a8cc44;
    --gold: #a89b2e;
    --gold-soft: #c2ad4c;
    --ink: #111111;
    --grey: #3a3a3a;
    --paper: #fbfbfb;
    --white: #ffffff;
  }
  * { box-sizing: border-box; margin: 0; padding: 0; }
  html, body { width: 1200px; height: 1200px; overflow: hidden; background: var(--paper); }
  .flyer { position: relative; width: 1200px; height: 1200px; background: var(--paper); font-family: "Rubik", sans-serif; overflow: hidden; }

  .hero { position: absolute; left: 0; top: 0; width: 1200px; height: 445px;
    background: linear-gradient(90deg, #1a66a3 0%, #2a78b3 45%, #1f6aa6 75%, #1b63a0 100%); }

  .brand-tab { position: absolute; left: 913px; top: 0; width: 223px; height: 222px; background: var(--white);
    border-radius: 0 0 26px 26px; display: flex; flex-direction: column; align-items: center; justify-content: center; gap: 12px; padding: 0 18px; text-align: center; }
  .brand-tab .dot { width: 36px; height: 36px; border-radius: 50%; background: var(--blue); }
  .brand-tab .name { font-family: "Rubik", sans-serif; font-weight: 600; font-size: 19px; line-height: 1.2; color: var(--blue); }

  .headline { position: absolute; left: 63px; top: 62px; font-weight: 700; font-size: 93px; line-height: 1; color: var(--green); letter-spacing: -0.5px; }
  .subhead { position: absolute; left: 64px; top: 165px; font-family: "Roboto Condensed", sans-serif; font-weight: 700; font-size: 50px; line-height: 72px; color: var(--white); }

  .photo { position: absolute; }
  .photo-selfie { left: 695px; top: 417px; width: 226px; height: 224px; background: linear-gradient(135deg, #6d9fc0 0%, #b7a18d 45%, #2a2c3a 100%); }
  .photo-car { left: 942px; top: 503px; width: 227px; height: 226px; background: linear-gradient(160deg, #b9c7a6 0%, #8a7a62 45%, #3b3f46 100%); }

  .benefits { position: absolute; left: 0; top: 486px; list-style: none; }
  .benefits li { position: relative; height: 66.5px; padding-left: 67px; font-weight: 500; font-size: 36px; line-height: 44px; color: var(--ink); }
  .benefits li::before { content: ""; position: absolute; left: 0; top: 9px; width: 38px; height: 22px; background: var(--gold); }

  .payout-band { position: absolute; left: 0; top: 774px; width: 1200px; height: 86px; background: var(--gold);
    display: flex; align-items: center; justify-content: center; font-family: "Roboto Condensed", sans-serif; font-weight: 700; font-size: 35px; color: var(--white); }

  .cta { position: absolute; left: 68px; top: 900px; font-weight: 600; font-size: 44px; line-height: 51px; }
  .cta .line-blue { color: var(--blue-deep); display: block; }
  .cta .line-green { color: var(--lime); display: block; }
  .phone { position: absolute; left: 68px; top: 1016px; display: flex; align-items: center; gap: 22px; font-weight: 600; font-size: 64px; color: var(--grey); }
  .phone svg { width: 58px; height: 46px; }

  .quick-links { position: absolute; top: 932px; left: 694px; display: flex; gap: 27px; }
  .quick-link { width: 124px; height: 124px; border-radius: 50%; display: flex; flex-direction: column; align-items: center; justify-content: center;
    color: var(--white); font-weight: 500; font-size: 13px; line-height: 1.05; text-align: center; gap: 4px; }
  .quick-link svg { width: 46px; height: 42px; }
  .ql-programs { background: var(--blue); }
  .ql-rates { background: var(--lime); }
  .ql-calc { background: var(--gold-soft); }

  .footer { position: absolute; left: 0; top: 1122px; width: 1200px; height: 78px; background: var(--blue);
    display: flex; align-items: center; justify-content: center; color: var(--white); font-weight: 500; font-size: 25px; }
  .footer span { padding: 0 28px; }
  .footer .sep { width: 2px; height: 40px; background: var(--white); padding: 0; }
</style>
</head>
<body>
<div class="flyer">
  <div class="hero" role="img" aria-label="Faded blue-tinted photo of a smiling family"></div>

  <div class="brand-tab">
    <div class="dot"></div>
    <div class="name">Harborline Financial Services, Inc.</div>
  </div>

  <h1 class="headline">62 or Older?</h1>
  <p class="subhead">A Reverse Mortgage<br>could be<br>Your Road To Financial Freedom</p>

  <div class="photo photo-selfie" role="img" aria-label="Photo of a smiling senior couple taking a selfie by the sea"></div>
  <div class="photo photo-car" role="img" aria-label="Photo of a laughing senior couple in a convertible car"></div>

  <ul class="benefits">
    <li>No Monthly Payments</li>
    <li>No Income Requirements</li>
    <li>No Credit Score Requirements</li>
    <li>No Loss of Ownership</li>
  </ul>

  <div class="payout-band">Receive cash by lump sum, monthly installments or a line of credit!!</div>

  <p class="cta"><span class="line-blue">Call us today for a</span><span class="line-green">Free Consultation!!</span></p>

  <div class="phone">
    <svg viewBox="0 0 58 46" aria-hidden="true">
      <path d="M2 16 C2 6 56 6 56 16 L56 20 L44 20 L44 14 C38 11 20 11 14 14 L14 20 L2 20 Z" fill="var(--blue)"/>
      <path d="M12 22 L46 22 L52 44 L6 44 Z" fill="var(--blue)"/>
      <g fill="var(--white)">
        <circle cx="22" cy="29" r="2"/><circle cx="29" cy="29" r="2"/><circle cx="36" cy="29" r="2"/>
        <circle cx="22" cy="35" r="2"/><circle cx="29" cy="35" r="2"/><circle cx="36" cy="35" r="2"/>
        <circle cx="22" cy="41" r="2"/><circle cx="29" cy="41" r="2"/><circle cx="36" cy="41" r="2"/>
      </g>
    </svg>
    <span>(800) 647-2915</span>
  </div>

  <nav class="quick-links">
    <div class="quick-link ql-programs">
      <svg viewBox="0 0 46 42" fill="none" stroke="#fff" stroke-width="2"><path d="M4 20 L20 6 L36 20"/><path d="M8 17 V38 H32 V17"/><rect x="12" y="24" width="8" height="8"/><circle cx="37" cy="16" r="7"/><path d="M34 20 L40 12"/></svg>
      <span>Loan<br>Programs</span>
    </div>
    <div class="quick-link ql-rates">
      <svg viewBox="0 0 46 42" fill="none" stroke="#fff" stroke-width="2"><path d="M7 20 L23 6 L39 20"/><path d="M11 17 V38 H35 V17"/><text x="23" y="33" fill="#fff" stroke="none" font-size="17" font-weight="700" text-anchor="middle" font-family="Rubik, sans-serif">$</text></svg>
      <span>Loan<br>Rates</span>
    </div>
    <div class="quick-link ql-calc">
      <svg viewBox="0 0 46 42" fill="none" stroke="#fff" stroke-width="2"><rect x="12" y="2" width="22" height="38" rx="2"/><rect x="16" y="6" width="14" height="8"/><rect x="16" y="18" width="5" height="5"/><rect x="25" y="18" width="5" height="5"/><rect x="16" y="27" width="5" height="5"/><rect x="25" y="27" width="5" height="5"/></svg>
      <span>Mortgage<br>Calculator</span>
    </div>
  </nav>

  <footer class="footer">
    <span>Harborline Financial Services, Inc.</span>
    <i class="sep"></i>
    <span>NMLS #517830</span>
    <i class="sep"></i>
    <span>www.harborlinefunds.example</span>
  </footer>
</div>
</body>
</html>
```